Instagram Business Card For Comedian

Hi,

I'd like a 2-sided business card that kind mimics an Instagram page. I've attached screenshots with the copy and language that should be written on there.

I'd like it to be way more stylized and a bit more creative than what I did on Powerpoint. I just did a mockup so that you can have an idea. I'd like it to be designed and you to take a bit of creative imagery so that it doesn't look so static and monochromatic.

PLEASE BE CREATIVE WITH THESE DESIGNS. I DON'T WANT IT TO LOOK EXACTLY LIKE THE ATTACHED IMAGE OR EXACTLY LIKE AN INSTAGRAM PAGE. I want to use it as inspiration to create something that looks more sleek, and creative. I don't want the colors to just be boring gray, and blue. Have fun and spice it up a bit!

Check out my website LornaFabish.com to see the colors and fonts I use for my branding.

For the main photo: Here's a link with the hi-res photo: !https://www.filecrate-example.com/s/q8ktw3rmpadvhje/Lorna-Fabish-C71B2204.jpg?dl=0

For the thumbnail icon photo, you can use this: https://www.filecrate-example.com/s/xo5nvte2gwhrbsk/Lorna%20Fabish%20Tin%20Vale%20Headshot.jpg?dl=0

Use the Standard Business Card Template from Quillprint.com:
https://help.quillprint-example.com/hc/en-us/article_attachments/309827164/Standard_Size__US__Business_Cards_Portrait.jpg

Please let me know if you have any questions.
Updates

Industry/Entity Type

Business

Contact Information for Business Card

All of the text and copy has been provided on the attached jpg.

Colors
33a6d7
0255a3
aaaaaa
dbdbdb
1b1b1b

Requirements
Should not have
• A Hyperlink for the Email Addresses

```html
<!DOCTYPE html>
<html lang="en">
<head>
<meta charset="utf-8">
<title>Lorna Fabish – Business Card</title>
<link rel="stylesheet" href="https://fonts.googleapis.com/css2?family=Source+Sans+3:ital,wght@0,400;0,600;1,400&display=swap">
<style>
  :root{
    --stage:#3d3938;
    --card-back:#e9e9e9;
    --band:#111111;
    --accent:#f05a57;
    --brand-blue:#33a6d7;
    --ink:#3a3a3a;
    --muted:#d0d0d0;
    --rule:#555555;
  }
  *{box-sizing:border-box;margin:0;padding:0}
  html,body{width:1200px;height:900px;overflow:hidden}
  body{background:var(--stage);font-family:"Source Sans 3",sans-serif;position:relative}

  .card{position:absolute;top:184px;height:491px;box-shadow:2px 3px 4px rgba(0,0,0,.45)}
  .card-front{left:322px;width:301px;background:var(--band)}
  .card-back{left:645px;width:305px;background:var(--card-back);color:var(--ink)}

  .portrait{position:absolute;left:0;top:0;width:301px;height:357px;
    background:
      radial-gradient(ellipse 60% 55% at 50% 45%, rgba(26,20,18,.85) 0%, rgba(26,20,18,.55) 45%, rgba(26,20,18,0) 80%),
      linear-gradient(180deg,#efe6dd 0%,#e9ddd2 55%,#f06d5a 80%,#ec6552 100%);}
  .front-band{position:absolute;left:0;top:357px;width:301px;height:134px;text-align:center}
  .front-name{margin-top:27px;font-size:32px;font-weight:600;color:var(--brand-blue);line-height:1}
  .front-roles{margin-top:13px;font-size:14.5px;color:var(--muted);letter-spacing:.2px}

  .back-inner{position:absolute;left:30px;top:35px;width:250px}
  .back-name{font-size:20px;font-weight:600;color:var(--accent);line-height:22px;letter-spacing:.3px}
  .back-roles{font-size:14.5px;line-height:18px;letter-spacing:.1px}
  .row{display:flex;align-items:center;gap:4px;line-height:19px;font-size:14.5px}
  .row svg{flex:none}
  .website{margin-top:9px;font-size:16px}
  .section-head{display:flex;align-items:center;gap:6px;color:var(--accent);font-size:16px;font-weight:600;line-height:20px;width:246px}
  .section-head::after{content:"";flex:1;height:1px;background:var(--rule)}
  .bookings{margin-top:18px}
  .about{margin-top:26px}
  .about-text{font-size:14.5px;line-height:18.5px;margin-top:2px;width:246px}
  .more{margin-top:12px}
  .social{margin-top:6px}
  .social .row{font-size:14.5px;line-height:20.5px;gap:3px}
  .sign-off{margin-top:3px;width:246px;text-align:center;font-style:italic;font-size:12px;color:var(--accent)}
</style>
</head>
<body>
  <section class="card card-front">
    <div class="portrait" role="img" aria-label="Portrait photo of Lorna Fabish with voluminous curly hair, wearing a coral top, against a light wall"></div>
    <div class="front-band">
      <p class="front-name">Lorna Fabish</p>
      <p class="front-roles">COMEDIAN | ACTOR | WRITER</p>
    </div>
  </section>

  <section class="card card-back">
    <div class="back-inner">
      <h1 class="back-name">LORNA FABISH</h1>
      <p class="back-roles">COMEDIAN | ACTOR | WRITER</p>
      <p class="row website">
        <svg width="13" height="13" viewBox="0 0 16 16" aria-hidden="true"><circle cx="8" cy="8" r="7.5" fill="#444"/><path d="M4 5c2 0 2 2 4 2s1 3 3 3M9 2c0 2 2 2 3 3M5 12c1-1 2-2 1-4" stroke="#e9e9e9" stroke-width="1.4" fill="none"/></svg>
        www.lornafabish.com
      </p>

      <h2 class="section-head bookings">For Bookings</h2>
      <p class="row"><svg width="12" height="10" viewBox="0 0 12 10" aria-hidden="true"><rect width="12" height="10" fill="#444"/><path d="M0.5 1l5.5 4.5L11.5 1" stroke="#e9e9e9" stroke-width="1.2" fill="none"/></svg>Dana@BrightlineTalentGroup.com</p>
      <p class="row"><svg width="12" height="10" viewBox="0 0 12 10" aria-hidden="true"><rect width="12" height="10" fill="#444"/><path d="M0.5 1l5.5 4.5L11.5 1" stroke="#e9e9e9" stroke-width="1.2" fill="none"/></svg>June.Harlow@ortiv.com</p>

      <h2 class="section-head about">About Me</h2>
      <p class="about-text">Stand Up Comedian. I Host. I write. I Dance. I Do Not Sing Unless I'm in the Shower. I Accept Tips. (Not on jokes, but on Paywisp.<br>As seen on Orbo, Laugh Channel, QTV, Dox TV, Kestrel, and UNB.</p>

      <h2 class="section-head more">More Info</h2>
      <div class="social">
        <p class="row"><svg width="18" height="18" viewBox="0 0 18 18" aria-hidden="true"><circle cx="9" cy="9" r="8" fill="none" stroke="#333" stroke-width="1.3"/></svg>Friendpage.com/lornafabish</p>
        <p class="row"><svg width="18" height="18" viewBox="0 0 18 18" aria-hidden="true"><circle cx="9" cy="9" r="8" fill="none" stroke="#333" stroke-width="1.3"/></svg>Chirpline.com/lornafab</p>
        <p class="row"><svg width="18" height="18" viewBox="0 0 18 18" aria-hidden="true"><circle cx="9" cy="9" r="8" fill="none" stroke="#333" stroke-width="1.3"/></svg>Photofeed.com/lornafab</p>
      </div>
      <p class="sign-off">Lets Stay Connected !</p>
    </div>
  </section>
</body>
</html>
```